Kestrel Signs Facebook Banner Design

Design a facebook banner for a sign company. I would like to have a modern approach to it.

Product Offering:
Signs
Banners
Decals
Commercial Wraps

```html
<!DOCTYPE html>
<html lang="en">
<head>
<meta charset="UTF-8">
<title>Kestrel Signs – Facebook Banner</title>
<link href="https://fonts.googleapis.com/css2?family=Montserrat:wght@500;600;700;800;900&display=swap" rel="stylesheet">
<style>
  :root{
    --stage:#c2c2c2;
    --bg-light:#fff3f0;
    --bg-pink:#fbd9d2;
    --red:#e8202a;
    --deep-red:#c8152a;
    --orange:#f7941d;
    --ink:#2f2f33;
    --ink-soft:#3c3c40;
    --dots:#f4a6a0;
  }
  *{box-sizing:border-box;margin:0;padding:0}
  html,body{width:900px;height:1200px;overflow:hidden}
  body{background:var(--stage);font-family:"Montserrat",sans-serif;color:var(--ink);position:relative}

  .banner{position:absolute;overflow:hidden;
    background:linear-gradient(115deg,var(--bg-light) 0%,#fde6e1 45%,var(--bg-pink) 100%);
    box-shadow:0 6px 10px rgba(0,0,0,.25)}
  .banner *{position:absolute}
  .banner--cover{left:64px;top:250px;width:771px;height:285px}
  .banner--compact{left:153px;top:620px;width:594px;height:311px}

  .swirl{border-radius:50%;background:rgba(248,190,180,.35)}
  .dot-field{background:var(--dots);opacity:.55;border-radius:3px}

  .brand-name{font-weight:900;color:var(--ink);line-height:.95;letter-spacing:.5px}

  .headline{font-weight:900;color:var(--red);line-height:1;letter-spacing:-.5px}
  .subline{font-weight:500;color:var(--ink);line-height:1.15}

  .services{border:2px solid var(--orange);border-radius:10px;background:rgba(255,255,255,.55)}
  .services-tag{border-radius:20px;background:linear-gradient(90deg,var(--orange),var(--red));
    color:#fff;font-weight:800;display:flex;align-items:center;justify-content:center;white-space:nowrap}
  .service{font-weight:800;color:var(--red);line-height:1.1;text-transform:uppercase}
  .service-note{font-weight:500;color:var(--ink);line-height:1.15;text-align:center}
  .rule-v{background:var(--red)}
  .rule-h{background:var(--red)}
  .rule-dark{background:var(--ink)}

  .offer{font-weight:600;color:var(--ink);white-space:nowrap}
  .phone{border-radius:20px;background:var(--orange);display:flex;align-items:center}
  .phone .arrow{position:relative;border-radius:50%;background:#fff;display:flex;align-items:center;justify-content:center;flex:none}
  .phone .number{position:relative;font-weight:800;color:var(--deep-red);white-space:nowrap}

  .footer{display:flex;align-items:center;white-space:nowrap}
  .footer > *{position:relative}
  .web{font-weight:600;letter-spacing:1.2px;color:var(--ink)}
  .footer .sep{width:1.5px;background:var(--orange);align-self:stretch}
  .social{display:flex}
  .social span{position:relative;border-radius:50%;background:var(--ink)}
  .handle{font-weight:600;color:var(--ink-soft)}
</style>
</head>
<body>

<!-- Wide cover -->
<section class="banner banner--cover" aria-label="Kestrel Signs cover banner">
  <div class="swirl" style="left:560px;top:-60px;width:260px;height:220px"></div>
  <div class="swirl" style="left:430px;top:180px;width:220px;height:160px"></div>
  <div class="dot-field" role="img" aria-label="Dot grid accent" style="left:327px;top:0;width:59px;height:16px"></div>
  <div class="dot-field" role="img" aria-label="Dot grid accent" style="left:17px;top:251px;width:59px;height:19px"></div>

  <div class="brand-name" style="left:25px;top:18px;font-size:22px">KESTREL<br><span style="position:static;padding-left:44px">SIGNS</span></div>

  <h1 class="headline" style="left:16px;top:78px;font-size:42px">ENHANCE<br>YOUR BRAND</h1>
  <p class="subline" style="left:17px;top:165px;font-size:27px">WITH HIGH QUALITY<br>DESIGN!</p>

  <div class="services" style="left:416px;top:44px;width:317px;height:176px"></div>
  <div class="services-tag" style="left:431px;top:31px;width:286px;height:24px;font-size:13.5px">DISCOVER OUR VARIOUS SERVICES</div>

  <div class="service" style="left:445px;top:74px;font-size:16px">Creative<br>Advertising</div>
  <div class="rule-v" style="left:576px;top:75px;width:2px;height:35px"></div>
  <div class="service" style="left:600px;top:74px;font-size:16px">Premium<br>Banners</div>
  <div class="rule-h" style="left:426px;top:122px;width:297px;height:2px"></div>
  <div class="service" style="left:445px;top:136px;font-size:16px">Unique<br>Decals</div>
  <div class="rule-v" style="left:576px;top:137px;width:2px;height:35px"></div>
  <div class="service" style="left:600px;top:136px;font-size:16px">Commercial<br>Wraps</div>

  <p class="offer" style="left:426px;top:183px;width:297px;text-align:center;font-size:12px">Contact us now &amp; get a special offer!</p>

  <div class="phone" style="left:481px;top:207px;width:191px;height:32px;padding-left:3px">
    <span class="arrow" style="width:26px;height:26px">
      <svg width="12" height="14" viewBox="0 0 12 14"><path d="M2 1l7 6-7 6" fill="none" stroke="#2f2f33" stroke-width="3"/></svg>
    </span>
    <span class="number" style="font-size:18px;margin-left:10px">+1 604-555-0148</span>
  </div>

  <div class="footer" style="left:414px;top:250px;height:18px;gap:10px">
    <span class="web" style="font-size:10.5px">WWW.KESTRELSIGNS.CA</span>
    <span class="sep"></span>
    <span class="social" style="gap:3px"><span style="width:12px;height:12px"></span><span style="width:12px;height:12px"></span><span style="width:12px;height:12px"></span><span style="width:12px;height:12px"></span><span style="width:12px;height:12px"></span><span style="width:12px;height:12px"></span></span>
    <span class="handle" style="font-size:10.5px">Kestrelsigns</span>
  </div>
</section>

<!-- Compact version -->
<section class="banner banner--compact" aria-label="Kestrel Signs compact banner">
  <div class="swirl" style="left:-60px;top:-30px;width:150px;height:260px"></div>
  <div class="swirl" style="left:500px;top:150px;width:160px;height:220px"></div>
  <div class="dot-field" role="img" aria-label="Dot grid accent" style="left:531px;top:15px;width:48px;height:16px"></div>
  <div class="dot-field" role="img" aria-label="Dot grid accent" style="left:15px;top:278px;width:48px;height:16px"></div>

  <div class="brand-name" style="left:0;width:594px;top:14px;text-align:center;font-size:16px">KESTREL<br>SIGNS</div>
  <div class="rule-dark" style="left:156px;top:52px;width:282px;height:1px;opacity:.35"></div>

  <h2 class="headline" style="left:0;width:594px;top:62px;text-align:center;font-size:26.5px">ENHANCE YOUR BRAND WITH</h2>
  <p class="subline" style="left:0;width:594px;top:91px;text-align:center;font-size:21px">HIGH QUALITY DESIGN!</p>

  <div class="services" style="left:64px;top:141px;width:467px;height:81px;border-width:1.5px"></div>
  <div class="services-tag" style="left:186px;top:131px;width:221px;height:18px;font-size:10px">DISCOVER OUR VARIOUS SERVICES</div>

  <div class="service" style="left:84px;width:104px;top:155px;text-align:center;font-size:10.5px">Creative<br>Advertising</div>
  <div class="service" style="left:190px;width:104px;top:155px;text-align:center;font-size:10.5px">Premium<br>Banners</div>
  <div class="service" style="left:296px;width:112px;top:155px;text-align:center;font-size:10.5px">Unique<br>Decals</div>
  <div class="service" style="left:410px;width:100px;top:155px;text-align:center;font-size:10.5px">Commercial<br>Wraps</div>

  <div class="rule-dark" style="left:84px;top:186px;width:426px;height:1.5px"></div>

  <div class="rule-dark" style="left:186px;top:163px;width:1.5px;height:17px"></div>
  <div class="rule-dark" style="left:291px;top:163px;width:1.5px;height:17px"></div>
  <div class="rule-dark" style="left:405px;top:163px;width:1.5px;height:17px"></div>
  <div class="rule-dark" style="left:186px;top:195px;width:1.5px;height:17px"></div>
  <div class="rule-dark" style="left:291px;top:195px;width:1.5px;height:17px"></div>
  <div class="rule-dark" style="left:405px;top:195px;width:1.5px;height:17px"></div>

  <p class="service-note" style="left:84px;width:104px;top:192px;font-size:9px">Highlighting your<br>brand identity</p>
  <p class="service-note" style="left:190px;width:104px;top:192px;font-size:9px">Durable and<br>eye-catching</p>
  <p class="service-note" style="left:292px;width:114px;top:192px;font-size:9px">Effective promotional<br>solutions</p>
  <p class="service-note" style="left:408px;width:104px;top:192px;font-size:9px">Make your products<br>stand out</p>

  <p class="offer" style="left:0;width:594px;top:232px;text-align:center;font-size:9.5px">Contact us now &amp; get a special offer!</p>

  <div class="phone" style="left:224px;top:250px;width:146px;height:25px;padding-left:2px">
    <span class="arrow" style="width:21px;height:21px">
      <svg width="9" height="11" viewBox="0 0 12 14"><path d="M2 1l7 6-7 6" fill="none" stroke="#2f2f33" stroke-width="3"/></svg>
    </span>
    <span class="number" style="font-size:14px;margin-left:7px">+1 604-555-0148</span>
  </div>

  <div class="footer" style="left:0;width:594px;justify-content:center;top:285px;height:14px;gap:7px">
    <span class="web" style="font-size:7.5px;letter-spacing:.6px">WWW.KESTRELSIGNS.CA</span>
    <span class="sep"></span>
    <span class="social" style="gap:2px"><span style="width:10px;height:10px"></span><span style="width:10px;height:10px"></span><span style="width:10px;height:10px"></span><span style="width:10px;height:10px"></span><span style="width:10px;height:10px"></span><span style="width:10px;height:10px"></span></span>
    <span class="handle" style="font-size:7.5px">Kestrelsigns</span>
  </div>
</section>

</body>
</html>
```